New high end server provider needs wordpress design

www.kv7hosting.com

Need a wordpress design for a high end server provider that provides overclocked dedicated servers for rent. We are located in Chicago but we have a presence is Virginia and Nevada for both our east and west coast customers.

We are a server provider that specializes in top end hardware with every feature designed for optimum performance. If it is not the best quality part or provides the best possible performance we don't run it. Our customers are mainly those that want the best single threaded performance possible from their hardware. We would be selling our services directly on our website via WHMCS.

We would like to see designs that are very modern and simplistic yet very attractive looking and catchy. Would prefer colors in the blues and greens and white. These colors are not necessary and I would be open to another color scheme if it looks good.

The final design should show speed and performance while being simplistic and easy on the eyes.

Logo and company name added and payment changed to guaranteed.  Looking for a wordpress template with the same pages as kv7hosting.com but with a redesigned look and feel.  

WHMCS control panel design also part of the design request.

If you have any questions please let me know!  This is just for kv7hosting.com and a main page for WHMCS (no coding just design).

Target Market(s)

IT Guru's (mostly men in their 20's to 30's)

Industry/Entity Type

Hardware

Requirements
Must have
• WHMCS panel design to fit with website theme.
Nice to have
• Main slider on home page similar to one of our other websites at www.kv7hosting.com
Should not have
• Flash or frames

```html
<!DOCTYPE html>
<html lang="en">
<head>
<meta charset="utf-8">
<title>KV7Hosting</title>
<link rel="stylesheet" href="https://fonts.googleapis.com/css2?family=Bebas+Neue&family=Oswald:wght@500;700&family=Play:wght@400;700&family=Roboto:wght@300;400&family=Arimo&display=swap">
<style>
:root{
  --ink-dark:#3a3a3a;
  --blue-head:#1b5a96;
  --accent-red:#e03a1e;
  --text-gray:#777;
  --title-gray:#5d5d5d;
  --link-blue:#1f8fc4;
  --panel-bg:#f6f6f6;
  --page-bg:#eeeeee;
  --band-gray:#8c8c8c;
  --partner-gray:#6f6f6f;
  --footer-bg:#1c2f3e;
  --footer-text:#b9c3cb;
  --footer-line:#2f4556;
  --bottom-bg:#050505;
  --bullet-blue:#8fc3dc;
}
*{margin:0;padding:0;box-sizing:border-box}
html,body{width:1200px;height:1092px;overflow:hidden;background:var(--page-bg)}
body{font-family:"Roboto",sans-serif;font-weight:300;color:var(--text-gray)}
.page{position:relative;width:1200px;height:1092px;overflow:hidden;background:var(--page-bg)}
.abs{position:absolute}

.top-strip{left:0;top:0;width:1200px;height:5px;background:#4a4a4a}
.site-header{left:0;top:5px;width:1200px;height:72px;background:linear-gradient(#f2f2f2,#e3e3e3)}
.brand{left:166px;top:20px;display:flex;align-items:center;gap:8px;font-family:"Play",sans-serif;font-weight:700;font-size:26px;color:#1d3b52}
.brand-dot{width:30px;height:30px;border-radius:50%;background:#1d3b52}
.main-nav{left:512px;top:28px;width:524px;display:flex;justify-content:space-between;font-family:"Oswald",sans-serif;font-weight:500;font-size:17px;color:var(--ink-dark);text-transform:uppercase;white-space:nowrap}

.hero{left:0;top:77px;width:1200px;height:329px;background:linear-gradient(90deg,#3d3d3d 0%,#8a8a8a 20%,#e8e8e8 36%,#f4f4f4 42%,#9a9a9a 55%,#4a4a4a 78%,#262626 100%)}
.hero-headline{left:164px;top:116px;width:525px;height:125px;background:rgba(255,255,255,.82);padding:10px 0 0 17px;font-family:"Bebas Neue",sans-serif;font-weight:400;font-size:48px;line-height:52px;color:var(--blue-head);text-transform:uppercase;white-space:nowrap;overflow:hidden}
.hero-points{left:164px;top:262px;width:387px;list-style:none}
.hero-points li{height:22px;display:flex;align-items:center;background:rgba(235,235,235,.92);font-family:"Arimo",sans-serif;font-size:11.5px;color:#333;border-bottom:1px solid #d0d0d0;white-space:nowrap}
.hero-points li i{width:21px;height:22px;background:var(--accent-red);margin-right:5px;display:flex;align-items:center;justify-content:center}
.slider-dots{left:966px;top:377px;display:flex;gap:5px}
.slider-dots span{width:12px;height:12px;background:#f2f2f2}
.slider-dots .active{background:var(--accent-red)}

.section-title{font-family:"Play",sans-serif;font-weight:400;font-size:22px;color:var(--title-gray);letter-spacing:.6px;white-space:nowrap}
.photo{box-shadow:0 2px 4px rgba(0,0,0,.35);border:1px solid #fff}
.welcome-title{left:163px;top:430px}
.welcome-photo{left:164px;top:468px;width:220px;height:140px;background:linear-gradient(135deg,#2a2a2a 0%,#5a6f8f 45%,#2d5fb0 60%,#1c1c1c 100%)}
.welcome-text{left:397px;top:466px;width:360px;font-size:12.2px;line-height:17.4px}
.offer-title{left:163px;top:640px}
.offer-photo{left:166px;top:678px;width:219px;height:138px;background:linear-gradient(120deg,#c98a7a 0%,#d9c2b8 35%,#cfd3d8 60%,#3a3a3a 100%)}
.offer-list{left:400px;top:677px;width:360px;list-style:none;font-size:12.2px;line-height:17.4px}
.offer-list li{position:relative;padding-left:26px;margin-bottom:3.5px}
.offer-list li::before{content:"";position:absolute;left:0;top:2px;width:13px;height:13px;border-radius:50%;background:var(--bullet-blue)}

.tweets{left:780px;top:436px;width:255px;height:389px;background:var(--panel-bg)}
.tweets-title{left:17px;top:6px}
.tweet{position:absolute;left:16px;display:flex;gap:9px}
.tweet-avatar{width:64px;height:54px;background:#fff;border:1px solid #ccc;display:flex;align-items:center;justify-content:center;flex:none}
.tweet-avatar span{width:36px;height:36px;border-radius:50%;background:#1d3b52}
.tweet-body{font-family:"Play",sans-serif;font-size:10.5px;line-height:15.7px;color:#666;width:160px}
.tweet-body b{display:block;color:var(--link-blue);font-weight:400}
.tweet-body a{color:var(--link-blue);text-decoration:underline;white-space:nowrap;letter-spacing:-.2px}
.view-all{left:17px;top:347px;width:56px;height:22px;background:linear-gradient(#e8632f,#c9431a);color:#fff;font-size:10.5px;font-weight:400;display:flex;align-items:center;justify-content:center}

.partners{left:0;top:847px;width:1200px;height:82px;background:var(--band-gray)}
.partner{position:absolute;background:var(--partner-gray)}

.site-footer{left:0;top:929px;width:1200px;height:131px;background:var(--footer-bg)}
.footer-col{position:absolute;top:16px}
.footer-col h3{font-family:"Play",sans-serif;font-weight:400;font-size:16px;color:#fff;letter-spacing:.5px;margin-bottom:10px;white-space:nowrap}
.footer-col p{font-size:10.8px;line-height:15.7px;color:var(--footer-text);width:320px}
.footer-col ul{list-style:none;font-size:10.8px;line-height:17.5px;color:var(--footer-text);white-space:nowrap}
.footer-col li{padding-left:17px;position:relative}
.footer-col li::before{content:"→";position:absolute;left:0;font-size:9px;color:#8a98a3}
.footer-col li.plain::before{content:""}
.footer-divider{position:absolute;top:18px;width:1px;height:105px;background:var(--footer-line)}

.bottom-bar{left:0;top:1060px;width:1200px;height:32px;background:var(--bottom-bg);font-size:10.8px;color:#ddd;font-weight:400}
.bottom-bar .copy{position:absolute;left:168px;top:9px}
.bottom-bar .credit{position:absolute;right:162px;top:9px}
</style>
</head>
<body>
<div class="page">
  <div class="abs top-strip"></div>
  <header class="abs site-header">
    <div class="abs brand"><span class="brand-dot"></span>KV7Hosting</div>
    <nav class="abs main-nav"><span>Home</span><span>Our Servers</span><span>Dedicated Servers</span><span>Why KV7?</span><span>Contacts</span></nav>
  </header>

  <section class="abs hero" role="img" aria-label="Photo of a long aisle of server racks in a data center"></section>
  <div class="abs hero-headline">Speeds that set us<br>apart from the competition</div>
  <ul class="abs hero-points">
    <li><i><svg width="8" height="10" viewBox="0 0 8 10"><path d="M1 1l5 4-5 4" stroke="#fff" stroke-width="2" fill="none"/></svg></i>Lorem Ipsum is that it has a more-or-less normal.</li>
    <li><i><svg width="8" height="10" viewBox="0 0 8 10"><path d="M1 1l5 4-5 4" stroke="#fff" stroke-width="2" fill="none"/></svg></i>Distribution of letters, as opposed to using 'Content here.</li>
    <li><i><svg width="8" height="10" viewBox="0 0 8 10"><path d="M1 1l5 4-5 4" stroke="#fff" stroke-width="2" fill="none"/></svg></i>Lorem Ipsum making it look like readable English.</li>
  </ul>
  <div class="abs slider-dots"><span class="active"></span><span></span><span></span><span></span></div>

  <h2 class="abs section-title welcome-title">Welcome to KV7Hosting</h2>
  <div class="abs photo welcome-photo" role="img" aria-label="Close-up of a motherboard heatsink with blue accents"></div>
  <p class="abs welcome-text">Lorem Ipsum is that it has a more-or-less normal distribution of letters, as opposed to using content look like readable English. Many desktop publishing packages and web page editors now use Lorem Ipsum as their default model text, and a search for normal distribution of letters, as opposed to using Many desktop their default and will uncover many web sites still in their infancy. Lorem Ipsum is that like readable English.</p>

  <h2 class="abs section-title offer-title">What we offer</h2>
  <div class="abs photo offer-photo" role="img" aria-label="Hand installing a hard drive into a server"></div>
  <ul class="abs offer-list">
    <li>Best performing Frontier Siege 2 servers currently on the market.</li>
    <li>Built in FS2 web-admin panel.</li>
    <li>Personal and dedicated customer support.</li>
    <li>Unlimited Player Slots on all game servers.</li>
    <li>CorePanel control panel for easy server administration.</li>
  </ul>

  <aside class="abs tweets">
    <h2 class="abs section-title tweets-title">KV7Hosting Tweets</h2>
    <div class="tweet" style="top:44px"><div class="tweet-avatar"><span></span></div><div class="tweet-body"><b>KV7Hosting</b>4 SEO Tasks Small Businesses Must Do Every Month.<br><a>http://k7.co/8HDjl6kg Via # SEW</a></div></div>
    <div class="tweet" style="top:118px"><div class="tweet-avatar"><span></span></div><div class="tweet-body"><b>KV7Hosting</b>SEO Fail! 10 Most Commonly Overused Techniques Website.<br><a>http://k7.co/JAACZqRB Via # SEW</a></div></div>
    <div class="tweet" style="top:191px"><div class="tweet-avatar"><span></span></div><div class="tweet-body"><b>KV7Hosting</b>SEO Fail! 10 Most Commonly Overused Techniques Website.<br><a>http://k7.co/JAACZqRB Via # SEW</a></div></div>
    <div class="tweet" style="top:269px"><div class="tweet-avatar"><span></span></div><div class="tweet-body"><b>KV7Hosting</b>SEO Fail! 10 Most Commonly Overused Techniques Website.<br><a>http://k7.co/JAACZqRB Via # SEW</a></div></div>
    <div class="abs view-all">View all</div>
  </aside>

  <section class="abs partners" aria-label="Partners">
    <div class="partner" style="left:168px;top:26px;width:140px;height:28px;border-radius:4px"></div>
    <div class="partner" style="left:368px;top:23px;width:56px;height:34px;border-radius:50%"></div>
    <div class="partner" style="left:498px;top:29px;width:106px;height:22px;border-radius:3px"></div>
    <div class="partner" style="left:671px;top:19px;width:68px;height:43px;border-radius:5px"></div>
  </section>

  <footer class="abs site-footer">
    <div class="footer-col" style="left:168px"><h3>Ask Us A Question</h3><p>Lorem Ipsum is that it has a more-or-less normal distribution of letters, as opposed to using 'Content here, content here', making it look like readable English.</p></div>
    <div class="footer-divider" style="left:518px"></div>
    <div class="footer-col" style="left:538px"><h3>Our Services</h3><ul><li>Game Servers</li><li>Dedicated Servers</li></ul></div>
    <div class="footer-divider" style="left:673px"></div>
    <div class="footer-col" style="left:697px"><h3>Our Company</h3><ul><li>About US</li><li>FAQs</li><li>Testimonials</li><li>Contact Us</li></ul></div>
    <div class="footer-divider" style="left:825px"></div>
    <div class="footer-col" style="left:848px"><h3>Frontier Siege 2</h3><ul><li>Buy Frontier Siege 2</li><li class="plain">Northgate Studios</li><li class="plain">FS2HD</li></ul></div>
  </footer>
  <div class="abs bottom-bar"><span class="copy">Copyright © 2013 Meridian Projects Pacific.</span><span class="credit">Powerd by : Pixelcraft Studio</span></div>
</div>
</body>
</html>
```